***Design a Nutritional Supplement Label for Bright Harvest!***

I have an existing label, I want to keep the logo but change the rest of the design. I am open to different creative ideas, but it needs to look appropriate for the shelves at Bright Harvest. This means it needs to look professional and premium, without being sterile and boring. I feel like my current label looks a little 1990s. You can play with the colors, font and design elements, while keeping the logo, descriptive text and the same layout. Feel free to take some bold chances. (You cannot change the font in the supplement facts section)

Font styles to use
Sans Serif

Colors

Designer to choose colors to be used in the design.

Requirements
Must have
• Keep the same text and layout. Keep the "Muscle Haven" logo as-is. DO NOT CHANGE THE LOGO!!

```html
<!DOCTYPE html>
<html lang="en">
<head>
<meta charset="utf-8">
<title>Muscle Haven – Supplement Label</title>
<link href="https://fonts.googleapis.com/css2?family=Montserrat:wght@800&family=Open+Sans:wght@700;800&display=swap" rel="stylesheet">
<style>
  :root {
    --backdrop: #3d7954;
    --label-white: #ffffff;
    --leaf-light: #c8df8e;
    --leaf-mid: #8fbf3c;
    --leaf-deep: #3f8a22;
    --brand-blue: #0a78c2;
    --badge-blue: #0a8fd6;
    --badge-cyan: #0aa6e6;
    --pill-green: #8cbb35;
    --ink-white: #ffffff;
  }
  * { box-sizing: border-box; margin: 0; padding: 0; }
  html, body {
    width: 1200px; height: 675px; overflow: hidden;
    background: var(--backdrop);
  }
  .canvas {
    position: relative; width: 1200px; height: 675px;
    display: flex; align-items: center; justify-content: center;
  }
  .label {
    position: relative; width: 540px; height: 566px;
    background: var(--label-white); overflow: hidden;
  }
  .label__waves {
    position: absolute; inset: 0;
    background:
      radial-gradient(ellipse 62% 40% at 50% 52%, rgba(255,255,255,1) 45%, rgba(255,255,255,0) 100%),
      linear-gradient(180deg, var(--leaf-mid) 0%, var(--leaf-light) 22%, #eef5dc 45%, #eef5dc 62%, var(--leaf-light) 82%, var(--leaf-mid) 100%);
  }
  .label__waves::after {
    content: ""; position: absolute; left: 0; right: 0; top: 0; height: 10px;
    background: var(--leaf-deep); opacity: .55;
  }
  .brand {
    position: absolute; left: 0; right: 0; top: 150px;
    text-align: center; color: var(--brand-blue);
    font-family: "Montserrat", sans-serif; font-weight: 800;
  }
  .brand__first { display: block; font-size: 96px; line-height: 1; letter-spacing: 1px; }
  .brand__second { display: block; font-size: 54px; line-height: 1; letter-spacing: 30px; margin-top: 18px; padding-left: 30px; }
  .claims {
    position: absolute; top: 356px; left: 0; right: 0;
    display: flex; justify-content: center; gap: 20px;
  }
  .claim {
    width: 192px; height: 76px; border-radius: 10px;
    display: flex; align-items: center; justify-content: center; text-align: center;
    color: var(--ink-white); font-family: "Open Sans", sans-serif; font-weight: 700;
    font-size: 25px; line-height: 1;
  }
  .claim--absorption { background: var(--badge-blue); }
  .claim--speed { background: var(--badge-cyan); }
  .count {
    position: absolute; left: 50%; top: 478px; transform: translateX(-50%);
    width: 172px; height: 66px; border-radius: 33px; background: var(--pill-green);
    color: var(--ink-white); text-align: center; font-family: "Montserrat", sans-serif;
    font-weight: 800; padding-top: 14px;
  }
  .count__qty { display: block; font-size: 20px; letter-spacing: .5px; line-height: 1; }
  .count__type { display: block; font-size: 10px; margin-top: 5px; letter-spacing: .3px; }
</style>
</head>
<body>
  <main class="canvas">
    <section class="label">
      <div class="label__waves" role="img" aria-label="Flowing layered green wave lines across the label"></div>
      <h1 class="brand">
        <span class="brand__first">MUSCLE</span>
        <span class="brand__second">HAVEN</span>
      </h1>
      <div class="claims">
        <div class="claim claim--absorption">High<br>Absorption</div>
        <div class="claim claim--speed">Fast<br>Acting</div>
      </div>
      <div class="count">
        <span class="count__qty">100 CAPSULE</span>
        <span class="count__type">DIETARY SUPPLEMENT</span>
      </div>
    </section>
  </main>
</body>
</html>
```